Hip / Cool Business Card for Custom Accessory Company

I would like to get a 2 sided design for standard size business cards, glossy (2 inches x 3.5 inches). Can be landscape or portrait layout! The design should include our logo (attached). The card should be extremely clear that the company is Tin Lantern. Should also have our URL clear. Should also use the color scheme seen on our upcoming site, tinlantern-example.com. The font we use is called "hurry up." Other than that, please go-to-town. We are targeting 15-45 y.o. market, with a skew on the 20-30 crowd. We do custom and stock phone cases as well as Cufflinks, Winestoppers; see the website for more.
Updates

Project Deadline Extended
Reason: Extending in case the US July 4th Holiday is keeping people from working!!

Industry/Entity Type

Landscape

Requirements
Must have
• Must be clear that the website is tinlantern-example.com. Must be clear that custom designs are an option.
Nice to have
• images of our designs. examples of our designs.
Should not have
• hard on the eyes contrasting colors such as orange on black. green on blue. Should not have any fonts that are considered "old" like Times New Roman. But decorative fonts are fine.

```html
<!DOCTYPE html>
<html lang="en">
<head>
<meta charset="utf-8">
<title>Tin Lantern – Business Card Designs</title>
<link rel="stylesheet" href="https://fonts.googleapis.com/css2?family=Audiowide&display=swap">
<style>
  :root {
    --backdrop: #3a302c;
    --card: #ffffff;
    --teal: #1ba3ad;
    --teal-soft: #d3eef0;
    --ink: #111111;
    --label: #f4f1ec;
  }
  * { box-sizing: border-box; margin: 0; padding: 0; }
  html, body { width: 1200px; height: 900px; overflow: hidden; }
  body {
    background: var(--backdrop);
    font-family: "Audiowide", sans-serif;
    position: relative;
  }
  .design-label {
    position: absolute;
    color: var(--label);
    font-size: 26px;
    letter-spacing: 1px;
  }
  .design-label--one { left: 130px; top: 56px; }
  .design-label--two { left: 970px; top: 520px; }

  .card {
    position: absolute;
    width: 420px;
    height: 240px;
    background: var(--card);
    border-radius: 16px;
    overflow: hidden;
    box-shadow: 0 6px 18px rgba(0,0,0,.45);
  }
  .card-bands { position: absolute; inset: 0; width: 100%; height: 100%; }
  .card--d1-back  { left: 90px;  top: 120px; }
  .card--d1-front { left: 690px; top: 120px; }
  .card--d2-back  { left: 90px;  top: 590px; }
  .card--d2-front { left: 690px; top: 590px; }

  .brand {
    position: absolute;
    display: flex;
    align-items: center;
    gap: 10px;
  }
  .brand-dot {
    width: 60px; height: 60px;
    border-radius: 50%;
    background: var(--teal);
    flex: none;
  }
  .brand-name {
    color: var(--ink);
    font-size: 26px;
    line-height: 1.02;
    text-transform: uppercase;
  }
  .card--d1-back .brand { left: 150px; top: 80px; }
  .card--d1-front .brand,
  .card--d2-front .brand { right: 24px; top: 126px; }
  .card--d2-back .brand { left: 18px; top: 88px; }

  .faint-mark {
    position: absolute;
    left: -40px; top: 30px;
    width: 170px; height: 170px;
    border-radius: 50%;
    background: var(--teal-soft);
    opacity: .7;
  }

  .name-tab {
    position: absolute;
    left: 22px; top: 12px;
    width: 170px; height: 26px;
    background: var(--teal);
    color: #fff;
    font-size: 13px;
    padding: 5px 14px;
    border-radius: 0 4px 4px 0;
  }
  .role { position: absolute; left: 40px; top: 42px; font-size: 10px; color: var(--ink); }

  .contact-list {
    position: absolute;
    left: 22px; top: 62px;
    list-style: none;
    font-size: 9px;
    color: var(--ink);
  }
  .contact-list li { display: flex; align-items: center; gap: 8px; margin-bottom: 6px; }
  .contact-icon {
    width: 15px; height: 15px;
    border: 1px solid var(--teal);
    background: var(--teal-soft);
    display: flex; align-items: center; justify-content: center;
  }
  .contact-icon svg { width: 10px; height: 10px; }

  .web-address {
    position: absolute;
    left: 28px; bottom: 24px;
    color: var(--teal);
    font-size: 12px;
    letter-spacing: 3px;
    text-transform: uppercase;
  }

  .product-list {
    position: absolute;
    right: 14px; top: 20px;
    list-style: none;
    text-align: right;
    font-size: 10px;
    color: var(--teal);
    text-transform: uppercase;
  }
  .product-list li {
    display: flex; justify-content: flex-end; align-items: center;
    gap: 6px; margin-bottom: 7px;
  }
  .product-bullet {
    width: 13px; height: 13px; border-radius: 50%;
    background: var(--teal);
  }
  .custom-note {
    position: absolute;
    right: 18px; bottom: 40px;
    font-size: 9px;
    color: var(--teal);
    text-transform: uppercase;
  }
</style>
</head>
<body>

  <p class="design-label design-label--one">DESIGN 1</p>
  <p class="design-label design-label--two">DESIGN 2</p>

  <section class="card card--d1-back" aria-label="Design 1 logo side">
    <svg class="card-bands" viewBox="0 0 420 240" aria-hidden="true">
      <polygon points="0,40 330,14 330,20 0,50" fill="#1ba3ad"/>
      <polygon points="130,236 420,208 420,218 150,240" fill="#1ba3ad"/>
    </svg>
    <div class="faint-mark" role="img" aria-label="Faint oversized brand mascot decoration"></div>
    <div class="brand">
      <span class="brand-dot"></span>
      <span class="brand-name">Tin<br>Lantern</span>
    </div>
  </section>

  <section class="card card--d1-front" aria-label="Design 1 contact side">
    <svg class="card-bands" viewBox="0 0 420 240" aria-hidden="true">
      <polygon points="192,20 420,20 420,30 200,30" fill="#1ba3ad"/>
      <polygon points="0,220 300,220 310,232 0,232" fill="#1ba3ad"/>
    </svg>
    <div class="name-tab">YOUR NAME</div>
    <p class="role">CEO</p>
    <ul class="contact-list">
      <li><span class="contact-icon"><svg viewBox="0 0 10 10"><rect x="3" y="1" width="4" height="8" rx="1" fill="none" stroke="#1ba3ad"/></svg></span>+41 00 555 01 23</li>
      <li><span class="contact-icon"><svg viewBox="0 0 10 10"><rect x="1" y="2.5" width="8" height="5" fill="none" stroke="#1ba3ad"/><polyline points="1,2.5 5,5.5 9,2.5" fill="none" stroke="#1ba3ad"/></svg></span>HELLO@TINLANTERN-EXAMPLE.COM</li>
      <li><span class="contact-icon"><svg viewBox="0 0 10 10"><path d="M5 9 L2 5 A3 3 0 1 1 8 5 Z" fill="#1ba3ad"/></svg></span>RUE DES LANTERNES 12 LAUSANNE</li>
    </ul>
    <div class="brand">
      <span class="brand-dot"></span>
      <span class="brand-name">Tin<br>Lantern</span>
    </div>
    <p class="web-address">www.tinlantern-example.com</p>
  </section>

  <section class="card card--d2-back" aria-label="Design 2 product side">
    <svg class="card-bands" viewBox="0 0 420 240" aria-hidden="true">
      <polygon points="0,34 300,8 300,16 0,44" fill="#1ba3ad"/>
      <polygon points="120,236 420,210 420,220 140,240" fill="#1ba3ad"/>
    </svg>
    <div class="brand">
      <span class="brand-dot"></span>
      <span class="brand-name">Tin<br>Lantern</span>
    </div>
    <ul class="product-list">
      <li>Charm Bracelets <span class="product-bullet"></span></li>
      <li>Cufflinks <span class="product-bullet"></span></li>
      <li>Earrings <span class="product-bullet"></span></li>
      <li>Money Clips <span class="product-bullet"></span></li>
      <li>Necklaces <span class="product-bullet"></span></li>
      <li>Phone Cases <span class="product-bullet"></span></li>
      <li>Wine Stoppers <span class="product-bullet"></span></li>
    </ul>
    <p class="custom-note">We do custom and stock phone cases</p>
  </section>

  <section class="card card--d2-front" aria-label="Design 2 contact side">
    <svg class="card-bands" viewBox="0 0 420 240" aria-hidden="true">
      <polygon points="192,20 420,20 420,30 200,30" fill="#1ba3ad"/>
      <polygon points="0,220 300,220 310,232 0,232" fill="#1ba3ad"/>
    </svg>
    <div class="name-tab">YOUR NAME</div>
    <p class="role">CEO</p>
    <ul class="contact-list">
      <li><span class="contact-icon"><svg viewBox="0 0 10 10"><rect x="3" y="1" width="4" height="8" rx="1" fill="none" stroke="#1ba3ad"/></svg></span>+41 00 555 01 23</li>
      <li><span class="contact-icon"><svg viewBox="0 0 10 10"><rect x="1" y="2.5" width="8" height="5" fill="none" stroke="#1ba3ad"/><polyline points="1,2.5 5,5.5 9,2.5" fill="none" stroke="#1ba3ad"/></svg></span>HELLO@TINLANTERN-EXAMPLE.COM</li>
      <li><span class="contact-icon"><svg viewBox="0 0 10 10"><path d="M5 9 L2 5 A3 3 0 1 1 8 5 Z" fill="#1ba3ad"/></svg></span>RUE DES LANTERNES 12 LAUSANNE</li>
    </ul>
    <div class="brand">
      <span class="brand-dot"></span>
      <span class="brand-name">Tin<br>Lantern</span>
    </div>
    <p class="web-address">www.tinlantern-example.com</p>
  </section>

</body>
</html>
```